Carpal Tunnel - PPC Landing Page

We need to do a SINGLE page landing page for a doctor who specializes in Carpal Tunnel syndrome - please research if you're not familiar - it's very common.

Landing page essentials:
Must have a form in upper right hand corner:
Form title: "Get a free diagnosis."
Form inputs: Name, Phone, Email, Requested Appointment time

Page is for PPC, so needs to be simple and light on content. Content has been provided and attached to this project.

No navigation, just a single page.

Industry/Entity Type

Health

Coding

Coded - Design and coding required

Number of Pages Required

1 page

Requirements
Must have
• Elegant look - Conversion optimized for form and phone
• Responsive design.
Should not have
• Old outdated images.

```html
<!DOCTYPE html>
<html lang="en">
<head>
<meta charset="utf-8">
<title>Carpal Tunnel Care – Free Diagnosis</title>
<link href="https://fonts.googleapis.com/css2?family=Open+Sans:wght@300;400;600;700&display=swap" rel="stylesheet">
<style>
  :root{
    --green:#2f9a3f;
    --green-dark:#1f7a2e;
    --ink:#2b2b2b;
    --muted:#555;
    --hero-a:#f2f2f2;
    --hero-b:#d6d6d6;
    --line:#e3e3e3;
    --footer:#1d5e3a;
    --white:#fff;
  }
  *{box-sizing:border-box;margin:0;padding:0}
  html,body{width:723px;height:1200px;overflow:hidden;background:var(--white)}
  body{font-family:"Open Sans",Arial,sans-serif;color:var(--ink);position:relative}

  .topbar{position:absolute;left:0;top:0;width:723px;height:26px;background:var(--white);display:flex;justify-content:space-between;align-items:center;padding:0 22px}
  .brand{font-size:11px;font-weight:400;color:var(--muted)}
  .call{font-size:12px;font-weight:600;color:var(--green)}

  .hero{position:absolute;left:0;top:26px;width:723px;height:190px;background:linear-gradient(90deg,var(--hero-a) 0%,#e9e9e9 40%,var(--hero-b) 62%,#e4e4e4 100%)}
  .hero-photo{position:absolute;left:250px;top:0;width:240px;height:190px;background:radial-gradient(ellipse at 55% 55%,#e8c9b4 0%,#d7b39c 30%,rgba(215,215,215,0) 70%)}
  .hero-copy{position:absolute;left:22px;top:34px;width:240px}
  .hero-title{font-size:19px;font-weight:400;line-height:21px;color:#333;text-transform:uppercase;letter-spacing:.3px}
  .hero-title strong{display:block;font-size:21px;font-weight:400;color:var(--green)}
  .hero-text{margin-top:20px;font-size:6px;line-height:8.5px;color:#444}
  .hero-text p+p{margin-top:6px}

  .diagnosis-form{position:absolute;left:560px;top:8px;width:148px}
  .form-title{font-size:15px;font-weight:300;line-height:16px;color:#333}
  .form-title span{display:block;font-size:19px;text-transform:uppercase;font-weight:400}
  .field{display:block;width:148px;height:15px;margin-top:5px;background:var(--white);border:1px solid #cfcfcf;font-size:6px;color:#888;padding:3px 6px}
  .field:first-of-type{margin-top:8px}
  .field-label{font-size:6px;color:#555;margin-top:6px}
  .field-select{margin-top:2px;width:60px;display:flex;justify-content:space-between}
  .submit{display:block;margin-top:8px;width:148px;height:17px;background:var(--green);color:var(--white);font-size:10px;font-weight:600;text-align:center;line-height:17px;letter-spacing:.5px}

  .section-head{position:absolute;left:0;top:236px;width:723px;text-align:center;color:var(--green)}
  .section-head h2{font-size:15px;font-weight:600;line-height:17px}
  .section-head p{font-size:14px;font-weight:300;line-height:16px}

  .condition{position:absolute}
  .condition h3{font-size:9px;font-weight:700;color:#333;margin-bottom:8px;padding-bottom:3px}
  .condition-body{display:flex;gap:12px}
  .condition-photo{flex:0 0 108px;height:95px;background:linear-gradient(135deg,#efe3da,#d9bfae 60%,#c9d6e2)}
  .condition-photo.xray{background:linear-gradient(135deg,#1a1a1a,#6a6a6a 55%,#2a2a2a)}
  .condition-text{font-size:5.8px;line-height:8.2px;color:#555}
  .col-left{left:30px;width:322px}
  .col-right{left:372px;width:328px}
  .rule{position:absolute;left:30px;width:670px;height:1px;background:var(--line)}

  .footer{position:absolute;left:0;top:1160px;width:723px;height:40px;background:var(--footer);color:#d8ead9;padding:7px 22px;font-size:5.5px;line-height:7.5px;display:flex;justify-content:space-between}
  .footer strong{font-weight:600;color:var(--white)}
  .footer .copy{align-self:flex-end}
</style>
</head>
<body>
  <header class="topbar">
    <div class="brand">Clinic Name (logo)</div>
    <div class="call">Call: 0190 2211 47</div>
  </header>

  <section class="hero">
    <div class="hero-photo" role="img" aria-label="Photo of a person holding a sore wrist, pain area glowing red"></div>
    <div class="hero-copy">
      <h1 class="hero-title">World class<br>service at<strong>competitive rates</strong></h1>
      <div class="hero-text">
        <p>In Dr. Halvorsen's clinical practice, Carpal Tunnel Syndrome is one of the most commonly reported health problems. Carpal tunnel occurs when swelling pinches the median nerve, which provides sensation to the palm side of the thumb, index finger, middle finger and half of the ring finger.</p>
        <p>The result can be a mix of tingling, numbness, weakness and pain in the fingers, thumb, palm or forearm. If the condition is not treated, permanent loss of muscle tissue can occur.</p>
      </div>
    </div>
    <form class="diagnosis-form">
      <div class="form-title">Get a free<span>Diagnosis</span></div>
      <div class="field">First Name</div>
      <div class="field">Last Name</div>
      <div class="field">Phone</div>
      <div class="field">Email</div>
      <div class="field-label">Appointment time</div>
      <div class="field field-select"><span>9:00 am</span><span>▾</span></div>
      <div class="submit">SUBMIT</div>
    </form>
  </section>

  <div class="section-head">
    <h2>Other conditions treated</h2>
    <p>by Dr. Halvorsen</p>
  </div>

  <article class="condition col-left" style="top:296px">
    <h3>Cubital Tunnel Syndrome (Cell Phone Elbow)</h3>
    <div class="condition-body">
      <div class="condition-photo" role="img" aria-label="Photo of a person holding their elbow"></div>
      <p class="condition-text">Similar to carpal tunnel syndrome, cubital tunnel syndrome is a condition brought on by increased pressure. This occurs when there is increased pressure of the ulnar nerve at the elbow. The funny bone is on the inner portion of the elbow. Holding the elbow bent for long periods, such as while on the phone, can stretch and irritate the nerve, causing numbness in the ring and small fingers.</p>
    </div>
  </article>
  <article class="condition col-right" style="top:296px">
    <h3>DeQuervain Tenosynovitis</h3>
    <div class="condition-body">
      <div class="condition-photo" role="img" aria-label="Photo of a hand with pain at the base of the thumb"></div>
      <p class="condition-text">Also known as first dorsal compartment tenosynovitis, this is where one of the most common hand problems seen by hand surgeons. It is most common in women and new mothers. Essentially, this is a condition brought on by irritation or inflammation of the tendons around the base of the thumb. The swelling causes pain when grasping, making a fist or turning the wrist.</p>
    </div>
  </article>

  <div class="rule" style="top:548px"></div>

  <article class="condition col-left" style="top:562px">
    <h3>Dupuytren's Disease</h3>
    <div class="condition-body">
      <div class="condition-photo" role="img" aria-label="Photo of a palm with a bent ring finger"></div>
      <p class="condition-text">Dupuytren's Disease is caused by an abnormal thickening in the palm and fingers. This thickening tissue can form firm lumps and cords that pull the fingers down into the palm. It is most common in men over fifty and often runs in families. As the cords tighten, the fingers cannot be fully straightened, which makes daily tasks such as shaking hands or wearing gloves difficult.</p>
    </div>
  </article>
  <article class="condition col-right" style="top:562px">
    <h3>Hand Sprains</h3>
    <div class="condition-body">
      <div class="condition-photo" role="img" aria-label="Photo of a hand being examined for a sprain"></div>
      <p class="condition-text">Sprains result from forcing a joint to perform a function against its normal range of motion. Finger sprains occur when the ligaments, which are attached to the bone, are overstretched and the result is pain, swelling and stiffness. Sprains are common in sports and falls and are graded by severity. Mild sprains heal with rest, while severe ones may need splinting or repair.</p>
    </div>
  </article>

  <div class="rule" style="top:818px"></div>

  <article class="condition" style="left:30px;top:830px;width:670px">
    <h3>Hand Fractures</h3>
    <div class="condition-body">
      <div class="condition-photo xray" role="img" aria-label="X-ray image of a hand"></div>
      <p class="condition-text">Fractures of the fingers occur when the finger or hands hit a solid object with force. Fractures are most common at the base of the little finger. This is called a boxer's fracture. Nerve injuries can be a result of trauma, compression or overstretching. Nerves send impulses to the brain about sensation and also play an important role in finger movement. When nerves are injured, one can lose ability to move fingers, and sensation and feeling in the hand. There is a wide range of treatment options, from simple splinting to surgery. Early care gives the best chance of full recovery, so please book an appointment if you have pain, swelling or a change in how your hand moves after an injury.</p>
    </div>
  </article>

  <footer class="footer">
    <div>
      <strong>Clinic Name (Logo)</strong><br>
      100 Sample Street, Suite 4, Example City<br>
      Tel: 0190 2211 47
    </div>
    <div class="copy">© Clinic Name. All rights reserved.</div>
  </footer>
</body>
</html>
```